Brightwater Charity Ball Poster

We are looking for a poster for our upcoming event, "Brightwater Charity Ball" - a sit down dinner formal event hosted by our university club, OKRU.
Usually we source designs internally from our committee (even if they aren't the most amazing quality), however this time round we have no one available to do it as everyone is a volunteer.
The event's theme is 'winter wonderland', based around the snowy forests you see in Veltmoor or Crown of Ashes (neither of these specific things are the theme however). Our venue is a clear-roof marque in a space surrounded by very tall pine trees giving off the forest vibe, and there are festoons strung between the trees so this is an element of warm light amongst the forest, perhaps a building or village tucked away in the forest.
The poster is for printing out at A3 size, and we will also need to create a Facebook event cover photo and other marketing graphics from the original poster files so some flexibility in the design and original files are required.
Things that need to be included on the poster :
---Event details
Brightwater Charity Ball
Saturday 12th August
7pm – midnight
Halberd Auditorium, KPC
Tables of 10
Members - $140
Non members - $150
All profits donated to Stride for Hope
---- Extra info and images (can be at the bottom, in corners etc,)
18+ ID required | Drink Responsibly
OKRU Logo
KPC Union Logo
(these logos may be changed to black and white if need be)
Example images of styles, colours and the sort of landscape we want for the poster can be found in the document attached.

```html
<!DOCTYPE html>
<html lang="en">
<head>
<meta charset="utf-8">
<title>Brightwater Charity Ball</title>
<link rel="stylesheet" href="https://fonts.googleapis.com/css2?family=Ultra&family=Roboto:wght@300;400;500;700&display=swap">
<style>
  :root {
    --night: #1f2747;
    --dusk: #4a3f5c;
    --bark: #6b4a3e;
    --glow: #f4a23c;
    --frost: rgba(232, 233, 238, 0.86);
    --ink: #111111;
    --snow: #ffffff;
  }
  html, body {
    margin: 0;
    padding: 0;
    width: 921px;
    height: 1200px;
    overflow: hidden;
    background: #e4e7e4;
  }
  .poster {
    position: relative;
    width: 921px;
    height: 1200px;
    overflow: hidden;
    font-family: "Roboto", Arial, sans-serif;
  }
  .forest-scene {
    position: absolute;
    inset: 0;
    background:
      radial-gradient(circle at 97% 19%, rgba(255, 196, 90, 0.95) 0, rgba(244, 162, 60, 0.55) 5%, rgba(244, 162, 60, 0) 22%),
      radial-gradient(ellipse at 20% 20%, rgba(40, 52, 96, 0.9) 0, rgba(40, 52, 96, 0) 45%),
      linear-gradient(180deg, #2c3458 0%, var(--dusk) 18%, var(--bark) 32%, #7a6a78 42%, #c9c8d2 60%, #8c90a8 80%, var(--night) 100%);
  }
  .rule {
    position: absolute;
    left: 282px;
    width: 357px;
    height: 4px;
  }
  .rule--top { top: 80px; background: var(--snow); }
  .rule--venue { top: 541px; background: var(--ink); }
  .event-title {
    position: absolute;
    left: 0;
    top: 90px;
    width: 921px;
    height: 150px;
  }
  .event-title text {
    font-family: "Ultra", "Rockwell Extra Bold", Georgia, serif;
    font-size: 62px;
    fill: var(--snow);
    letter-spacing: 1px;
  }
  .event-subtitle {
    position: absolute;
    top: 193px;
    width: 100%;
    text-align: center;
    margin: 0;
    color: var(--snow);
    font-weight: 500;
    font-size: 27px;
  }
  .info-panel {
    position: absolute;
    left: 0;
    top: 503px;
    width: 921px;
    height: 571px;
    background: var(--frost);
  }
  .venue {
    position: absolute;
    top: 562px;
    width: 100%;
    margin: 0;
    text-align: center;
    color: var(--ink);
    font-weight: 700;
    font-size: 56px;
    line-height: 62px;
    letter-spacing: 0.16em;
    text-indent: 0.16em;
  }
  .date-box {
    position: absolute;
    left: 203px;
    top: 760px;
    width: 512px;
    height: 97px;
    box-sizing: border-box;
    background: var(--ink);
    border: 2px solid #cfcfcf;
    color: var(--snow);
    font-weight: 300;
    font-size: 35px;
    line-height: 42px;
    text-align: center;
    padding-top: 6px;
  }
  .partner {
    position: absolute;
    top: 886px;
    display: flex;
    align-items: center;
    gap: 10px;
    color: var(--ink);
    font-weight: 700;
    font-size: 24px;
  }
  .partner--union { left: 268px; }
  .partner--club { left: 528px; }
  .partner-dot {
    width: 40px;
    height: 40px;
    border-radius: 50%;
    background: var(--ink);
  }
  .ticket-info {
    position: absolute;
    top: 950px;
    width: 100%;
    margin: 0;
    text-align: center;
    color: var(--ink);
    font-size: 19px;
    line-height: 28px;
  }
  .ticket-info strong { font-weight: 500; }
  .fine-print {
    position: absolute;
    top: 1040px;
    width: 100%;
    margin: 0;
    text-align: center;
    color: var(--ink);
    font-size: 17px;
  }
</style>
</head>
<body>
<main class="poster">
  <div class="forest-scene" role="img" aria-label="Snowy winter forest of tall dark trees with warm sunlight glowing through the branches"></div>

  <div class="rule rule--top"></div>
  <svg class="event-title" viewBox="0 0 921 150" aria-label="Brightwater">
    <path id="title-arc" d="M70 120 Q460 40 851 120" fill="none"/>
    <text text-anchor="middle"><textPath href="#title-arc" startOffset="50%">BRIGHTWATER</textPath></text>
  </svg>
  <p class="event-subtitle">CHARITY BALL</p>

  <section class="info-panel"></section>
  <div class="rule rule--venue"></div>
  <h2 class="venue">HALBERD<br>AUDITORIUM<br>KPC</h2>

  <div class="date-box">SATURDAY 12TH AUGUST<br>7PM - MIDNIGHT</div>

  <div class="partner partner--union"><span class="partner-dot"></span>KPC Union</div>
  <div class="partner partner--club"><span class="partner-dot"></span>OKRU</div>

  <p class="ticket-info"><strong>Tables of 10</strong> &nbsp;|&nbsp; Members - $140 &nbsp;|&nbsp; Non members - $150<br>All profits donated to Stride for Hope</p>

  <p class="fine-print">18+ ID required / Drink Responsibly</p>
</main>
</body>
</html>
```